Aerospace & Defense Manufacturing Firm

Brochure for a contract manufacturing service provider in precision sheet metal, precision machining, complicated assemblies, and welding. We specialize in fast turnaround support in Military, Defense, Aerospace, High Technology and Automotive sectors.

Target Market(s)

Manufacturing OEMs

Font styles to use
Sans Serif

Requirements
Must have
• S standout brocure with specifics about what we do
Nice to have
• Looking for a standard or tri-fold brochure with catches the eye of our target audience, corporate procurement agents.
Should not have
• Anything that is informal or trendy. The target audience is large multi-national corproations, so anything "locally cool or hype" might not be appropriate.

```html
<!DOCTYPE html>
<html lang="en">
<head>
<meta charset="utf-8">
<title>Veltrane Industrial Manufacturing – Brochure</title>
<link href="https://fonts.googleapis.com/css2?family=Open+Sans:wght@300;400;600;700&display=swap" rel="stylesheet">
<style>
  :root{
    --navy:#14305a;
    --navy-deep:#0e2346;
    --blue:#2d8fd2;
    --blue-light:#5bb3e6;
    --blue-mid:#3c9edb;
    --steel:#a9b2bc;
    --paper:#ffffff;
    --ink:#2c3440;
    --muted:#7a8591;
    --stage:#e6e8eb;
  }
  *{box-sizing:border-box;margin:0;padding:0}
  html,body{width:841px;height:1200px;overflow:hidden}
  body{background:var(--stage);font-family:"Open Sans",Arial,sans-serif;color:var(--ink);position:relative}
  .spread{position:absolute;left:30px;width:781px;height:552px;background:var(--paper);display:flex;box-shadow:0 2px 10px rgba(0,0,0,.12)}
  .spread--outside{top:36px}
  .spread--inside{top:612px;display:block}
  .panel{position:relative;width:50%;height:100%;overflow:hidden}
  .panel + .panel{border-left:1px solid #e3e6ea}
  .photo{position:absolute;display:block}

  /* back cover */
  .badges{position:absolute;left:30px;top:30px;display:flex;gap:10px;align-items:center}
  .badge{width:38px;height:38px;border-radius:50%;background:#d8dde3;border:2px solid #b9c2cc}
  .badges__note{font-size:8px;color:var(--muted);width:120px;line-height:1.4;margin-left:6px}
  .contact-title{position:absolute;left:30px;top:178px;font-size:22px;font-weight:300;color:var(--blue)}
  .contact-rule{position:absolute;left:30px;top:212px;width:330px;height:1px;background:var(--blue-light)}
  .back-photo-a{left:30px;top:228px;width:160px;height:110px;background:linear-gradient(135deg,#cfd8e2,#6f8396)}
  .back-photo-b{left:200px;top:228px;width:160px;height:110px;background:linear-gradient(135deg,#a8b4c0,#3e4f60)}
  .contact-band{position:absolute;left:0;right:0;bottom:0;height:200px;background:var(--navy);padding:26px 30px}
  .contact-list{list-style:none}
  .contact-list li{display:flex;align-items:center;gap:10px;color:#dfe8f2;font-size:11px;margin-bottom:14px}
  .contact-list svg{width:18px;height:18px;flex:none}

  /* front cover */
  .brand{position:absolute;right:30px;top:30px;display:flex;align-items:center;gap:8px;font-size:22px;font-weight:600;color:var(--navy)}
  .brand__mark{width:14px;height:14px;background:var(--blue)}
  .front-photo-a{right:0;top:120px;width:220px;height:110px;background:linear-gradient(160deg,#9fc4e3,#4a6c8a 60%,#2a3c52)}
  .front-photo-b{right:0;top:234px;width:220px;height:100px;background:linear-gradient(160deg,#b9c1c9,#5b6570)}
  .front-band{position:absolute;left:0;right:0;bottom:0;height:218px;background:var(--navy-deep)}
  .front-band__lines{position:absolute;inset:0;background:repeating-linear-gradient(90deg,rgba(255,255,255,.04) 0 1px,transparent 1px 26px)}
  .title-box{position:absolute;left:150px;top:250px;width:150px;height:120px;background:var(--blue);padding:16px 14px;color:#fff;font-size:17px;font-weight:300;line-height:1.25}

  /* inside */
  .grid{position:absolute;inset:0;display:grid;grid-template-columns:repeat(5,1fr);grid-template-rows:36px 114px 100px 1fr}
  .intro-head{grid-column:1;grid-row:1;display:flex;align-items:center;gap:8px;padding-left:14px;font-size:17px;font-weight:600;color:var(--navy)}
  .intro-head::before{content:"";width:4px;height:20px;background:var(--blue)}
  .intro-text{grid-column:1;grid-row:2 / 4;padding:8px 14px;font-size:9px;line-height:1.55;color:var(--muted)}
  .sector-head{grid-row:1;display:flex;align-items:center;padding:0 10px;color:#fff;font-size:9.5px;font-weight:700;text-transform:uppercase;letter-spacing:.3px;line-height:1.15}
  .sector-head--a{grid-column:2;background:var(--blue)}
  .sector-head--b{grid-column:3;background:var(--blue-mid)}
  .sector-head--c{grid-column:4;background:var(--blue-light)}
  .sector-head--d{grid-column:5;background:var(--blue-mid)}
  .sector-text{grid-row:2;padding:10px;font-size:9px;line-height:1.5;color:var(--muted);border-left:1px solid #eef0f3}
  .sector-photo{grid-row:3;position:relative}
  .sector-photo--a{grid-column:2;background:linear-gradient(160deg,#d7b089,#7a5638)}
  .sector-photo--b{grid-column:3;background:linear-gradient(160deg,#c7cfd6,#5c6873)}
  .sector-photo--c{grid-column:4;background:linear-gradient(160deg,#a9b8c6,#4c5d6e)}
  .sector-photo--d{grid-column:5;background:linear-gradient(160deg,#b9c0c7,#4f5760)}
  .services{grid-column:1;grid-row:4;background:var(--navy);padding:16px 0}
  .services__title{color:#fff;font-size:20px;font-weight:300;line-height:1.15;padding:0 14px 14px;border-left:4px solid var(--blue);margin-left:0}
  .services__list{list-style:none}
  .services__list li{color:#fff;font-size:9.5px;font-weight:600;padding:9px 14px;border-top:1px solid rgba(255,255,255,.18)}
  .parts-photo{grid-column:2 / 6;grid-row:4;background:radial-gradient(ellipse at 50% 45%,#e8ebee,#a7afb8 70%,#7d8791)}
</style>
</head>
<body>

<section class="spread spread--outside">
  <div class="panel panel--back">
    <div class="badges">
      <span class="badge"></span>
      <span class="badge"></span>
      <p class="badges__note">Certified to quality and aerospace standards</p>
    </div>
    <h2 class="contact-title">Contact Us</h2>
    <div class="contact-rule"></div>
    <div class="photo back-photo-a" role="img" aria-label="Photo of a CNC machining centre at work"></div>
    <div class="photo back-photo-b" role="img" aria-label="Photo of machined metal components"></div>
    <div class="contact-band">
      <ul class="contact-list">
        <li><svg viewBox="0 0 20 20"><circle cx="10" cy="10" r="9" fill="#2d8fd2"/><path d="M7 5l2 3-1 1c.6 1.3 1.7 2.4 3 3l1-1 3 2-1 2c-4 0-8-4-8-8z" fill="#fff"/></svg>(555) 014-2290</li>
        <li><svg viewBox="0 0 20 20"><circle cx="10" cy="10" r="9" fill="#2d8fd2"/><rect x="5" y="6.5" width="10" height="7" fill="none" stroke="#fff" stroke-width="1.3"/><path d="M5 7l5 4 5-4" fill="none" stroke="#fff" stroke-width="1.3"/></svg>info@veltrane-mfg.example</li>
        <li><svg viewBox="0 0 20 20"><circle cx="10" cy="10" r="9" fill="#2d8fd2"/><path d="M10 4a4 4 0 0 1 4 4c0 3-4 8-4 8s-4-5-4-8a4 4 0 0 1 4-4z" fill="#fff"/><circle cx="10" cy="8" r="1.5" fill="#2d8fd2"/></svg>1200 Harbor Works Rd, Northfield</li>
        <li><svg viewBox="0 0 20 20"><circle cx="10" cy="10" r="9" fill="#2d8fd2"/><circle cx="10" cy="10" r="5" fill="none" stroke="#fff" stroke-width="1.3"/><path d="M5 10h10M10 5c-2 3-2 7 0 10M10 5c2 3 2 7 0 10" fill="none" stroke="#fff" stroke-width="1"/></svg>www.veltrane-mfg.example</li>
      </ul>
    </div>
  </div>

  <div class="panel panel--front">
    <div class="brand"><span class="brand__mark"></span>Veltrane</div>
    <div class="photo front-photo-a" role="img" aria-label="Photo of a naval ship at sea"></div>
    <div class="photo front-photo-b" role="img" aria-label="Photo of industrial manufacturing equipment"></div>
    <div class="front-band"><div class="front-band__lines"></div></div>
    <h1 class="title-box">Veltrane Industrial Manufacturing</h1>
  </div>
</section>

<section class="spread spread--inside">
  <div class="grid">
    <h2 class="intro-head">What we do?</h2>
    <p class="intro-text">Veltrane Industrial Manufacturing is a contract manufacturer of precision machined and fabricated parts, complex assemblies and welding, offering fast turnaround for OEMs worldwide. Our team delivers certified quality from prototype to full production.</p>

    <h3 class="sector-head sector-head--a">Aerospace</h3>
    <h3 class="sector-head sector-head--b">Military<br>Defense</h3>
    <h3 class="sector-head sector-head--c">High<br>Technology</h3>
    <h3 class="sector-head sector-head--d">Electronics<br>&amp; Automotive</h3>

    <p class="sector-text" style="grid-column:2">Flight-critical components machined and inspected to strict aerospace tolerances.</p>
    <p class="sector-text" style="grid-column:3">Durable parts and assemblies built for defense programs and rugged field use.</p>
    <p class="sector-text" style="grid-column:4">Precision enclosures and chassis for high technology and instrument makers.</p>
    <p class="sector-text" style="grid-column:5">Brackets, housings and welded frames for electronics and automotive lines.</p>

    <div class="sector-photo sector-photo--a" role="img" aria-label="Photo of a rocket launch"></div>
    <div class="sector-photo sector-photo--b" role="img" aria-label="Photo of military equipment"></div>
    <div class="sector-photo sector-photo--c" role="img" aria-label="Photo of high-tech machinery"></div>
    <div class="sector-photo sector-photo--d" role="img" aria-label="Photo of an automotive production line"></div>

    <div class="services">
      <h2 class="services__title">Our<br>Services</h2>
      <ul class="services__list">
        <li>Precision Machining</li>
        <li>Precision Sheet Metal Fabrication</li>
        <li>Complicated Assemblies</li>
        <li>Welding &amp; Fabricated Assemblies</li>
      </ul>
    </div>
    <div class="parts-photo" role="img" aria-label="Photo of an array of precision machined and sheet metal parts"></div>
  </div>
</section>

</body>
</html>
```